" Somos uma empresa afiliada a Corvena Capital e representamos ela em Cuiabá. Prestamos o serviço de assessoria em investimentos a clientes de alto poder aquisitivo, um público private. Serviço exclusivo de "

```html
<!DOCTYPE html>
<html lang="pt-BR">
<head>
<meta charset="utf-8">
<title>Vantor Investimentos – Blocos de Notas</title>
<link href="https://fonts.googleapis.com/css2?family=Cinzel:wght@500&family=Montserrat:wght@400;500&display=swap" rel="stylesheet">
<style>
  :root {
    --backdrop: #2e2f31;
    --navy: #0f2143;
    --navy-deep: #081530;
    --navy-light: #1c3563;
    --paper: #ffffff;
    --paper-shade: #eef0f3;
    --gold: #c8a45f;
    --gold-light: #e6cf98;
    --ink: #3a3f48;
  }
  * { margin: 0; padding: 0; box-sizing: border-box; }
  html, body { width: 1200px; height: 1200px; overflow: hidden; }
  body {
    background: var(--backdrop);
    position: relative;
    font-family: "Montserrat", sans-serif;
  }
  .sheet {
    position: absolute;
    width: 272px;
    height: 480px;
    overflow: hidden;
    box-shadow: 0 6px 18px rgba(0,0,0,.45);
  }
  .sheet--header { left: 464px; top: 80px; }
  .sheet--side   { left: 262px; top: 620px; }
  .sheet--cover  { left: 598px; top: 620px; }

  .sheet--header, .sheet--side {
    background: linear-gradient(135deg, var(--paper) 0%, var(--paper) 45%, var(--paper-shade) 100%);
  }
  .sheet--cover {
    background: radial-gradient(ellipse at 50% 45%, var(--navy-light) 0%, var(--navy) 55%, var(--navy-deep) 100%);
  }

  .watermark-area {
    position: absolute;
    left: 110px; top: 120px;
    width: 162px; height: 300px;
    background: linear-gradient(160deg, rgba(220,224,230,0) 0%, rgba(220,224,230,.55) 60%, rgba(220,224,230,0) 100%);
  }
  .sheet--cover .watermark-area {
    background: linear-gradient(160deg, rgba(40,70,120,0) 0%, rgba(40,70,120,.35) 60%, rgba(40,70,120,0) 100%);
  }

  .top-band {
    position: absolute; left: 0; top: 0;
    width: 100%; height: 40px;
    background: linear-gradient(90deg, var(--navy-deep), var(--navy-light) 50%, var(--navy-deep));
    display: flex; align-items: center; justify-content: center;
  }
  .top-band::after {
    content: ""; position: absolute; left: 0; bottom: 0;
    width: 100%; height: 2px;
    background: linear-gradient(90deg, transparent, var(--gold-light), transparent);
  }

  .brand { display: flex; align-items: center; gap: 6px; white-space: nowrap; }
  .brand__mark { width: 8px; height: 8px; background: var(--gold); flex: none; }
  .brand__name {
    font-family: "Cinzel", serif; font-weight: 500;
    line-height: 1; letter-spacing: .04em;
  }
  .brand--small .brand__name { font-size: 10px; color: var(--gold-light); }
  .brand--dark .brand__name { font-size: 10px; color: var(--navy); }
  .brand--large { gap: 8px; }
  .brand--large .brand__mark { width: 12px; height: 12px; }
  .brand--large .brand__name { font-size: 15px; color: var(--gold-light); }

  .sheet--side .brand { position: absolute; left: 24px; top: 20px; }
  .sheet--cover .brand {
    position: absolute; left: 50%; top: 47%;
    transform: translate(-50%, -50%);
  }

  .footer {
    position: absolute; left: 10px; right: 10px; bottom: 10px;
    display: flex; align-items: flex-end; gap: 8px;
  }
  .contact {
    font-size: 3.6px; line-height: 1.55; color: var(--ink);
    list-style: none; width: 48px; white-space: nowrap;
  }
  .footer__rule {
    flex: 1; height: 2px; margin-bottom: 2px;
    background: linear-gradient(90deg, var(--navy) 0%, var(--gold) 55%, var(--gold-light) 100%);
  }
  .partner { display: flex; align-items: center; gap: 3px; white-space: nowrap; }
  .partner__mark { width: 6px; height: 6px; background: var(--navy); }
  .partner__name { font-size: 6px; color: var(--ink); }

  .cover-rule {
    position: absolute; left: 0; bottom: 38px;
    width: 100%; height: 2px;
    background: linear-gradient(90deg, transparent, var(--gold) 20%, var(--gold-light) 50%, var(--gold) 80%, transparent);
  }
</style>
</head>
<body>

  <section class="sheet sheet--header">
    <div class="top-band">
      <div class="brand brand--small">
        <span class="brand__mark"></span>
        <span class="brand__name">VANTOR INVESTIMENTOS</span>
      </div>
    </div>
    <div class="watermark-area" role="img" aria-label="Faint large brand decoration"></div>
    <footer class="footer">
      <ul class="contact">
        <li>Av. Central, 1200</li>
        <li>Cuiabá – MT</li>
        <li>(65) 3000-0000</li>
        <li>vantorinvest.com.br</li>
      </ul>
      <div class="footer__rule"></div>
      <div class="partner">
        <span class="partner__mark"></span>
        <span class="partner__name">Corvena Capital</span>
      </div>
    </footer>
  </section>

  <section class="sheet sheet--side">
    <div class="brand brand--dark">
      <span class="brand__mark"></span>
      <span class="brand__name">VANTOR INVESTIMENTOS</span>
    </div>
    <div class="watermark-area" role="img" aria-label="Faint large brand decoration"></div>
    <footer class="footer">
      <ul class="contact">
        <li>Av. Central, 1200</li>
        <li>Cuiabá – MT</li>
        <li>(65) 3000-0000</li>
        <li>vantorinvest.com.br</li>
      </ul>
      <div class="footer__rule"></div>
      <div class="partner">
        <span class="partner__mark"></span>
        <span class="partner__name">Corvena Capital</span>
      </div>
    </footer>
  </section>

  <section class="sheet sheet--cover">
    <div class="watermark-area" role="img" aria-label="Faint large brand decoration"></div>
    <div class="brand brand--large">
      <span class="brand__mark"></span>
      <span class="brand__name">VANTOR INVESTIMENTOS</span>
    </div>
    <div class="cover-rule"></div>
  </section>

</body>
</html>
```